Card design for Heating and Cooling company

this is for a heating and cooling company we recently updated our logo and need to update our cards. We attached our logo so you can incorporate it into the card. We specialize in residential and commercial furnace and air condition repairs. Have been in business since 2014.

Phone number 555.284.9137

We need the following phrases
:Repairs, Installations, and maintenance
:Quality work at reasonable prices
:residential/commercial
:Licensed &Insured
:Email Pinegrovehvac47@mailbox-example.com
Name: Teodor K (Ted)
Also on back side I would like my logo with wording :Thank you for your business and refferal

Industry/Entity Type

Hvac

Contact Information for Business Card

:residential/commercial
:Licensed & Insured
Name: Teodor K (Ted)
Number:555.284.9136

Requirements
Must have
• Blue and red colors
Nice to have
• Maybe a pic of a furnace or air conditioner

```html
<!DOCTYPE html>
<html lang="en">
<head>
<meta charset="utf-8">
<title>Pinegrove Heating &amp; Cooling – Business Cards</title>
<link href="https://fonts.googleapis.com/css2?family=Work+Sans:wght@400;500;600;700&display=swap" rel="stylesheet">
<style>
  :root {
    --bg: #e6e8eb;
    --card: #ffffff;
    --blue: #2e9fdc;
    --red: #e8312b;
    --ink: #1d1d1f;
    --text: #3a3a3c;
    --muted: #4a4a4c;
  }
  * { box-sizing: border-box; margin: 0; padding: 0; }
  html, body {
    width: 1200px; height: 900px; overflow: hidden;
    background: var(--bg);
    font-family: "Work Sans", Arial, sans-serif;
  }
  .canvas { position: relative; width: 1200px; height: 900px; }
  .card {
    position: absolute; top: 296px;
    width: 540px; height: 309px;
    background: var(--card);
    box-shadow: 0 10px 30px rgba(0,0,0,.18);
    overflow: hidden;
  }
  .card--front { left: 40px; }
  .card--back { left: 620px; }

  .edge { position: absolute; top: 0; bottom: 0; width: 8px; }
  .edge--blue { left: 0; background: var(--blue); }
  .edge--red { right: 0; background: var(--red); }

  .brand {
    position: absolute; display: flex; align-items: center; gap: 8px;
  }
  .brand__dot {
    width: 22px; height: 22px; border-radius: 50%; background: var(--blue); flex: none;
  }
  .brand__name {
    font-weight: 700; color: var(--ink); line-height: 1.05;
    text-transform: uppercase; letter-spacing: .5px;
  }
  .card--front .brand { left: 120px; top: 62px; }
  .card--front .brand__name { font-size: 18px; }
  .card--back .brand { left: 190px; top: 100px; }
  .card--back .brand__name { font-size: 22px; }

  .checklist { position: absolute; list-style: none; }
  .checklist li {
    display: flex; align-items: center; gap: 4px;
    font-size: 13px; color: var(--muted); line-height: 22px;
  }
  .checklist svg { width: 9px; height: 9px; flex: none; }
  .checklist--services { left: 26px; top: 142px; }
  .checklist--scope { left: 300px; top: 228px; }
  .checklist--scope li { font-size: 14px; }

  .contact-name {
    position: absolute; left: 300px; top: 132px;
    font-size: 22px; font-weight: 600; color: var(--blue);
  }
  .contact-lines { position: absolute; left: 300px; top: 172px; list-style: none; }
  .contact-lines li {
    display: flex; align-items: center; gap: 5px;
    font-size: 12px; color: var(--text); line-height: 19px;
  }
  .contact-lines svg { width: 9px; height: 9px; flex: none; }

  .stripe { position: absolute; height: 3px; }
  .stripe--blue { background: var(--blue); }
  .stripe--red { background: var(--red); }
  .stripes-top .stripe { left: 0; width: 175px; }
  .stripes-top .stripe--blue { top: 82px; }
  .stripes-top .stripe--red { top: 92px; }
  .stripes-bottom .stripe { right: 0; width: 190px; }
  .stripes-bottom .stripe--blue { top: 190px; }
  .stripes-bottom .stripe--red { top: 200px; }

  .thanks {
    position: absolute; left: 40px; top: 222px;
    font-size: 11px; letter-spacing: 3px; color: var(--ink);
    text-transform: uppercase;
  }
</style>
</head>
<body>
<main class="canvas">

  <section class="card card--front" aria-label="Business card front">
    <div class="edge edge--blue"></div>
    <div class="edge edge--red"></div>

    <div class="brand">
      <span class="brand__dot"></span>
      <span class="brand__name">Pinegrove<br>Heating &amp; Cooling</span>
    </div>

    <ul class="checklist checklist--services">
      <li><svg viewBox="0 0 10 10"><path d="M1 5.5l2.5 2.5L9 1.5" fill="none" stroke="#e8312b" stroke-width="2"/></svg>Repairs, Installations, and maintenance</li>
      <li><svg viewBox="0 0 10 10"><path d="M1 5.5l2.5 2.5L9 1.5" fill="none" stroke="#e8312b" stroke-width="2"/></svg>Quality work at reasonable prices</li>
    </ul>

    <h1 class="contact-name">Teodor K</h1>
    <ul class="contact-lines">
      <li><svg viewBox="0 0 10 10"><rect x="2.5" y="0.5" width="5" height="9" rx="1" fill="none" stroke="#e8312b" stroke-width="1.2"/><circle cx="5" cy="7.8" r=".6" fill="#e8312b"/></svg>555.284.9137</li>
      <li><svg viewBox="0 0 10 10"><rect x="0.5" y="1.5" width="9" height="7" fill="#e8312b"/><path d="M0.5 1.5L5 5.5l4.5-4" fill="none" stroke="#fff" stroke-width="1"/></svg>Pinegrovehvac47@mailbox-example.com</li>
    </ul>

    <ul class="checklist checklist--scope">
      <li><svg viewBox="0 0 10 10"><path d="M1 5.5l2.5 2.5L9 1.5" fill="none" stroke="#e8312b" stroke-width="2"/></svg>Residential / Commercial</li>
      <li><svg viewBox="0 0 10 10"><path d="M1 5.5l2.5 2.5L9 1.5" fill="none" stroke="#e8312b" stroke-width="2"/></svg>Licensed &amp; Insured</li>
    </ul>
  </section>

  <section class="card card--back" aria-label="Business card back">
    <div class="stripes-top">
      <span class="stripe stripe--blue"></span>
      <span class="stripe stripe--red"></span>
    </div>
    <div class="brand">
      <span class="brand__dot"></span>
      <span class="brand__name">Pinegrove<br>Heating &amp; Cooling</span>
    </div>
    <div class="stripes-bottom">
      <span class="stripe stripe--blue"></span>
      <span class="stripe stripe--red"></span>
    </div>
    <p class="thanks">Thank you for your business and refferal</p>
  </section>

</main>
</body>
</html>
```